Alderwick Banner- Real Estate Luxury Sale Banner

I need a large banner for an outside of a construction building.

It should say
THE ALDERWICK
47 Alderwick Street, East Boston – A Boutique Collection of Four Luxury Residences

Experience refined living with elegant design, high-end finishes, and expansive private decks in every residence. Thoughtfully crafted for both comfort and sophistication, each home features a modern fireplace and exceptional attention to detail.

Residence One – 2 Bed | 3 Bath | Private Yard + Large Deck
Residence Two – 2 Bed | 2 Bath | Spacious Deck
Residence Three – 2 Bed | 2 Bath | Expansive Deck
Residence Four – 2 Bed | 2 Bath | Panoramic Roof Deck with Stunning Boston Views
Now Accepting Reservations – Limited Availability

Schedule Your Private Tour Today

Marisa Fenwald, Quillmoor Realty | 617-555-0192 | marisa@quillmoorhomes.com
Construction by Tarnell Build Group

Target Market(s)

ages 30-50

Industry/Entity Type

real estate

Font styles to use
Serif

Requirements
Must have
• classic look
Nice to have
• colors of navy and gold

```html
<!DOCTYPE html>
<html lang="en">
<head>
<meta charset="utf-8">
<title>The Alderwick – Quillmoor Realty</title>
<link rel="stylesheet" href="https://fonts.googleapis.com/css2?family=Cinzel:wght@500;600&family=Oswald:wght@600&family=Tinos:wght@400;700&display=swap">
<style>
  :root {
    --ink: #0d0d0f;
    --ink-soft: #1b1c20;
    --gold: #d9a441;
    --gold-soft: #c9963a;
    --white: #ffffff;
    --muted: #d8d8d8;
    --frame: #d7d7d7;
    --sky-top: #3d4656;
    --sky-low: #1d222b;
    --facade: #2c2e33;
    --facade-dark: #1c1d21;
    --wood: #a0785a;
    --room-bath: #cfd4d6;
    --room-bed: #6b5b52;
  }
  * { margin: 0; padding: 0; box-sizing: border-box; }
  html, body { width: 1200px; height: 500px; overflow: hidden; background: var(--ink); }

  .banner {
    position: relative;
    width: 1200px;
    height: 500px;
    overflow: hidden;
    background: linear-gradient(90deg, var(--ink) 0%, var(--ink-soft) 55%, var(--ink) 100%);
    border: 1px solid #444;
    font-family: "Tinos", "Times New Roman", serif;
    color: var(--white);
  }

  /* building photo */
  .building-photo {
    position: absolute;
    top: 0; right: 0;
    width: 380px; height: 500px;
    background:
      linear-gradient(90deg, var(--ink) 0%, rgba(13,13,15,0) 22%),
      linear-gradient(180deg, var(--sky-top) 0%, var(--sky-low) 100%);
  }
  .building-facade {
    position: absolute;
    left: 90px; top: 18px;
    width: 250px; height: 482px;
    background: linear-gradient(180deg, var(--facade) 0%, var(--facade-dark) 78%, var(--wood) 78%, var(--wood) 100%);
  }

  /* brand */
  .logo {
    position: absolute;
    left: 40px; top: 18px;
    width: 300px;
    text-align: center;
  }
  .logo-mark {
    display: block;
    width: 64px; height: 64px;
    margin: 0 auto 6px;
    border: 3px solid var(--gold);
    border-radius: 50%;
  }
  .logo-name {
    font-family: "Cinzel", "Times New Roman", serif;
    font-weight: 600;
    font-size: 28px;
    line-height: 1.05;
    letter-spacing: 1px;
    color: var(--gold);
  }

  /* headline */
  .headline {
    position: absolute;
    left: 40px; top: 156px;
    width: 300px;
    text-align: center;
    font-family: "Oswald", "Arial Narrow", sans-serif;
    font-weight: 600;
    font-size: 30px;
    line-height: 38px;
    letter-spacing: 1.5px;
    color: var(--white);
  }
  .address {
    position: absolute;
    left: 30px; top: 198px;
    width: 320px;
    text-align: center;
    font-size: 14px;
    line-height: 18px;
    color: var(--gold);
  }
  .tagline {
    position: absolute;
    left: 30px; top: 217px;
    width: 320px;
    text-align: center;
    font-size: 13px;
    line-height: 17px;
    font-style: normal;
    color: var(--muted);
  }

  /* features */
  .features { position: absolute; left: 56px; top: 248px; display: flex; gap: 34px; }
  .feature { display: flex; flex-direction: column; align-items: center; gap: 4px; }
  .feature svg { width: 48px; height: 40px; }
  .feature-label { font-size: 19px; line-height: 22px; }

  /* contact */
  .contact-title {
    position: absolute;
    left: 60px; top: 326px;
    font-size: 22px;
    font-weight: 400;
    letter-spacing: 1px;
    color: var(--gold);
  }
  .agent {
    position: absolute;
    left: 60px; top: 356px;
    font-size: 15px;
    color: var(--white);
  }
  .contact-line { position: absolute; left: 60px; display: flex; align-items: center; gap: 12px; font-size: 16px; }
  .contact-phone { top: 384px; }
  .contact-email { top: 412px; }
  .contact-line svg { width: 20px; height: 20px; }
  .builder {
    position: absolute;
    left: 60px; top: 456px;
    font-size: 13px;
    letter-spacing: .5px;
    color: var(--gold-soft);
  }

  /* gallery */
  .gallery-frame {
    position: absolute;
    background: var(--frame);
    clip-path: polygon(9% 0, 100% 0, 91% 100%, 0 100%);
  }
  .gallery-photo {
    position: absolute;
    inset: 5px;
    clip-path: polygon(9% 0, 100% 0, 91% 100%, 0 100%);
  }
  .gallery-bath { left: 350px; top: 26px; width: 420px; height: 150px; }
  .gallery-bath .gallery-photo {
    background: linear-gradient(90deg, #e9ecec 0%, #7aaec0 30%, var(--room-bath) 55%, #f2f2f2 75%, #8a6a50 100%);
  }
  .gallery-bed { left: 400px; top: 184px; width: 420px; height: 140px; }
  .gallery-bed .gallery-photo {
    background: linear-gradient(180deg, #8a7a70 0%, var(--room-bed) 45%, #4a3d3a 75%, #2b2422 100%);
  }

  /* residence details */
  .details {
    position: absolute;
    left: 372px; top: 338px;
    width: 440px;
    font-size: 12px;
    line-height: 14.5px;
    color: var(--muted);
  }
  .description { margin-bottom: 5px; }
  .residences { list-style: none; margin-bottom: 5px; }
  .residences strong { color: var(--white); font-weight: 700; }
  .availability { color: var(--gold); font-weight: 700; letter-spacing: .3px; }
  .tour { color: var(--white); font-weight: 700; letter-spacing: .3px; }
</style>
</head>
<body>
  <main class="banner">
    <div class="building-photo" role="img" aria-label="Photo of the four-storey dark-clad residential building at dusk">
      <div class="building-facade"></div>
    </div>

    <div class="logo">
      <span class="logo-mark"></span>
      <div class="logo-name">QUILLMOOR<br>REALTY</div>
    </div>

    <h1 class="headline">THE ALDERWICK</h1>
    <p class="address">47 Alderwick Street, East Boston</p>
    <p class="tagline">A Boutique Collection of Four Luxury Residences</p>

    <div class="gallery-frame gallery-bath">
      <div class="gallery-photo" role="img" aria-label="Photo of a bright modern bathroom with freestanding tub and walk-in shower"></div>
    </div>
    <div class="gallery-frame gallery-bed">
      <div class="gallery-photo" role="img" aria-label="Photo of a warmly lit bedroom with a made bed"></div>
    </div>

    <section class="details">
      <p class="description">Experience refined living with elegant design, high-end finishes, and expansive private decks in every residence. Thoughtfully crafted for both comfort and sophistication, each home features a modern fireplace and exceptional attention to detail.</p>
      <ul class="residences">
        <li><strong>Residence One</strong> – 2 Bed | 3 Bath | Private Yard + Large Deck</li>
        <li><strong>Residence Two</strong> – 2 Bed | 2 Bath | Spacious Deck</li>
        <li><strong>Residence Three</strong> – 2 Bed | 2 Bath | Expansive Deck</li>
        <li><strong>Residence Four</strong> – 2 Bed | 2 Bath | Panoramic Roof Deck with Stunning Boston Views</li>
      </ul>
      <p class="availability">Now Accepting Reservations – Limited Availability</p>
      <p class="tour">Schedule Your Private Tour Today</p>
    </section>

    <div class="features">
      <div class="feature">
        <svg viewBox="0 0 58 48" fill="none" stroke="var(--gold)" stroke-width="2.5" stroke-linejoin="round">
          <rect x="8" y="6" width="42" height="18" rx="3"/>
          <rect x="13" y="13" width="14" height="8" rx="2"/>
          <rect x="31" y="13" width="14" height="8" rx="2"/>
          <rect x="4" y="24" width="50" height="14" rx="2"/>
          <path d="M8 38v6M50 38v6"/>
        </svg>
        <span class="feature-label">2 Bed Rooms</span>
      </div>
      <div class="feature">
        <svg viewBox="0 0 58 48" fill="none" stroke="var(--gold)" stroke-width="2.5" stroke-linejoin="round">
          <path d="M10 24V8a5 5 0 0 1 10 0"/>
          <path d="M4 24h50"/>
          <path d="M8 24v8a10 10 0 0 0 10 10h22a10 10 0 0 0 10-10v-8"/>
          <path d="M14 42l-3 5M44 42l3 5"/>
          <path d="M34 6v12M40 4v14M46 6v12"/>
        </svg>
        <span class="feature-label">2 Bath Rooms</span>
      </div>
    </div>

    <h2 class="contact-title">CALLS US</h2>
    <p class="agent">Marisa Fenwald, Quillmoor Realty</p>

    <div class="contact-line contact-phone">
      <svg viewBox="0 0 24 24" fill="var(--gold)">
        <path d="M6.6 10.8a15.1 15.1 0 0 0 6.6 6.6l2.2-2.2a1 1 0 0 1 1-.25 11.4 11.4 0 0 0 3.6.57 1 1 0 0 1 1 1V20a1 1 0 0 1-1 1A17 17 0 0 1 3 4a1 1 0 0 1 1-1h3.5a1 1 0 0 1 1 1c0 1.25.2 2.450.57 3.57a1 1 0 0 1-.25 1z"/>
      </svg>
      <span>617-555-0192</span>
    </div>
    <div class="contact-line contact-email">
      <svg viewBox="0 0 24 24" fill="none" stroke="var(--gold)" stroke-width="1.8">
        <rect x="2" y="5" width="20" height="14"/>
        <path d="M2 5l10 8 10-8"/>
      </svg>
      <span>marisa@quillmoorhomes.com</span>
    </div>

    <p class="builder">Construction by Tarnell Build Group</p>
  </main>
</body>
</html>
```